Personal Training

Personal Fitness Trainer
Sports Nutritionist
Individual and Group rates available
Certifications
Global Wellness Coaching Federation
Continental Athletic Studies Council

Industry/Entity Type

Fitness

Contact Information for Business Card

Dorinda Pellham
555-284-7163
vetrubel4@quintmail.example

```html
<!DOCTYPE html>
<html lang="en">
<head>
<meta charset="utf-8">
<title>Dorinda Pellham – Personal Training Business Card</title>
<link rel="stylesheet" href="https://fonts.googleapis.com/css2?family=Lato:wght@400;700&display=swap">
<style>
  :root {
    --backdrop: #e9e9e9;
    --card-dark: #262626;
    --card-darker: #1b1b1b;
    --accent-red: #e4282c;
    --accent-red-soft: #ef3a3d;
    --icon-ink: #1e1e1e;
    --photo-light: #cfcac6;
    --photo-dark: #8f8a86;
  }
  * { margin: 0; padding: 0; box-sizing: border-box; }
  html, body {
    width: 1200px; height: 720px; overflow: hidden;
    background: var(--backdrop);
    font-family: "Lato", sans-serif;
  }
  .canvas { position: relative; width: 1200px; height: 720px; }
  .card {
    position: absolute; top: 205px;
    width: 540px; height: 309px;
    background: linear-gradient(135deg, var(--card-dark) 0%, var(--card-darker) 100%);
    overflow: hidden;
  }
  .card--front { left: 40px; }
  .card--back { left: 620px; }
  .band {
    position: absolute; left: 0; right: 0; height: 13px;
    background: linear-gradient(90deg, var(--accent-red), var(--accent-red-soft) 60%, var(--accent-red));
  }
  .band--top { top: 0; }
  .band--bottom { bottom: 0; }

  .portrait {
    position: absolute; left: 13px; top: 13px;
    width: 227px; height: 283px;
    background: linear-gradient(160deg, var(--photo-light) 0%, #b9b3ae 55%, var(--photo-dark) 100%);
  }
  .service-icons {
    position: absolute; top: 38px; left: 336px;
    display: flex; gap: 19px;
  }
  .service-icon {
    width: 45px; height: 45px; border-radius: 50%;
    background: var(--accent-red);
    display: flex; align-items: center; justify-content: center;
  }
  .service-icon svg { width: 28px; height: 28px; }
  .trainer-name {
    position: absolute; left: 280px; top: 141px;
    color: var(--accent-red);
    font-size: 20px; font-weight: 700; letter-spacing: 2px;
    line-height: 24px;
    text-transform: uppercase; white-space: nowrap;
  }
  .contact {
    position: absolute; left: 300px; top: 247px;
    color: var(--accent-red);
    font-size: 13.5px; letter-spacing: 0.9px; line-height: 20px;
    white-space: nowrap;
  }

  .service-list {
    position: absolute; left: 38px; top: 78px;
    list-style: none;
  }
  .service-list li {
    display: flex; align-items: center; gap: 8px;
    height: 26.3px;
    color: var(--accent-red);
    font-size: 12.6px; font-weight: 700; text-transform: uppercase;
    letter-spacing: -0.1px; white-space: nowrap;
  }
  .service-list svg { width: 20px; height: 20px; flex: none; }
</style>
</head>
<body>
<main class="canvas">

  <section class="card card--front" aria-label="Business card front">
    <div class="band band--top"></div>
    <div class="portrait" role="img" aria-label="Photo of the trainer standing outdoors in athletic wear"></div>

    <div class="service-icons">
      <span class="service-icon" aria-label="Heart health">
        <svg viewBox="0 0 24 24"><path fill="var(--icon-ink)" d="M12 21s-8-5.2-8-11a4.5 4.5 0 0 1 8-2.8A4.5 4.5 0 0 1 20 10c0 5.8-8 11-8 11z"/></svg>
      </span>
      <span class="service-icon" aria-label="Cardio training">
        <svg viewBox="0 0 24 24"><rect x="3" y="16" width="18" height="3" rx="1" fill="var(--icon-ink)"/><circle cx="9" cy="8" r="3" fill="var(--icon-ink)"/><rect x="11" y="11" width="9" height="2.5" rx="1" fill="var(--icon-ink)"/></svg>
      </span>
      <span class="service-icon" aria-label="Strength training">
        <svg viewBox="0 0 24 24"><g fill="var(--icon-ink)"><rect x="2" y="8" width="3" height="8" rx="1"/><rect x="5" y="6" width="3" height="12" rx="1"/><rect x="8" y="11" width="8" height="2"/><rect x="16" y="6" width="3" height="12" rx="1"/><rect x="19" y="8" width="3" height="8" rx="1"/></g></svg>
      </span>
    </div>

    <h1 class="trainer-name">Dorinda Pellham</h1>
    <p class="contact">555-284-7163<br>vetrubel4@quintmail.example</p>
    <div class="band band--bottom"></div>
  </section>

  <section class="card card--back" aria-label="Business card back">
    <div class="band band--top"></div>
    <ul class="service-list">
      <li><svg viewBox="0 0 24 24"><g fill="var(--accent-red)" transform="rotate(-45 12 12)"><rect x="1" y="9" width="3" height="6" rx="1"/><rect x="4" y="7" width="3" height="10" rx="1"/><rect x="7" y="11" width="10" height="2"/><rect x="17" y="7" width="3" height="10" rx="1"/><rect x="20" y="9" width="3" height="6" rx="1"/></g></svg>Personal Fitness Trainer</li>
      <li><svg viewBox="0 0 24 24"><g fill="var(--accent-red)" transform="rotate(-45 12 12)"><rect x="1" y="9" width="3" height="6" rx="1"/><rect x="4" y="7" width="3" height="10" rx="1"/><rect x="7" y="11" width="10" height="2"/><rect x="17" y="7" width="3" height="10" rx="1"/><rect x="20" y="9" width="3" height="6" rx="1"/></g></svg>Sports Nutritionist</li>
      <li><svg viewBox="0 0 24 24"><g fill="var(--accent-red)" transform="rotate(-45 12 12)"><rect x="1" y="9" width="3" height="6" rx="1"/><rect x="4" y="7" width="3" height="10" rx="1"/><rect x="7" y="11" width="10" height="2"/><rect x="17" y="7" width="3" height="10" rx="1"/><rect x="20" y="9" width="3" height="6" rx="1"/></g></svg>Individual and Group Rates Available</li>
      <li><svg viewBox="0 0 24 24"><g fill="var(--accent-red)" transform="rotate(-45 12 12)"><rect x="1" y="9" width="3" height="6" rx="1"/><rect x="4" y="7" width="3" height="10" rx="1"/><rect x="7" y="11" width="10" height="2"/><rect x="17" y="7" width="3" height="10" rx="1"/><rect x="20" y="9" width="3" height="6" rx="1"/></g></svg>Certifications</li>
      <li><svg viewBox="0 0 24 24"><g fill="var(--accent-red)" transform="rotate(-45 12 12)"><rect x="1" y="9" width="3" height="6" rx="1"/><rect x="4" y="7" width="3" height="10" rx="1"/><rect x="7" y="11" width="10" height="2"/><rect x="17" y="7" width="3" height="10" rx="1"/><rect x="20" y="9" width="3" height="6" rx="1"/></g></svg>Global Wellness Coaching Federation</li>
      <li><svg viewBox="0 0 24 24"><g fill="var(--accent-red)" transform="rotate(-45 12 12)"><rect x="1" y="9" width="3" height="6" rx="1"/><rect x="4" y="7" width="3" height="10" rx="1"/><rect x="7" y="11" width="10" height="2"/><rect x="17" y="7" width="3" height="10" rx="1"/><rect x="20" y="9" width="3" height="6" rx="1"/></g></svg>Continental Athletic Studies Council</li>
    </ul>
    <div class="band band--bottom"></div>
  </section>

</main>
</body>
</html>
```